Law Firm Logo and Stationary

I need a logo for my law firm.  The logo should only contain the firm name "Harlow & Harlow, P.C." but we are open to slight additions like underlining or a box.  We are looking for a modern style but not edgy because our target market is businesses and corporations.

I would like a logo that invokes the traditional values of a law firm (trust, integrity, knowledge) but I want an updated look.

To be clear, the logo should only contain the firm name, I am just looking for a font treatment.

The logo color is up to you.  The only initial opinion I have is that bright colors may not fit with the professional look of a law firm. 

I also want to incorporate the new logo into letterhead and business card designs.  The letterhead should include all of the information that is in my current letterhead, which is attached.  The letterhead should be black or grey on white.  The colored logo will go on the website and promotional materials.

For the business card, I would like to have the logo on the top left, the employee name (Colin J. Harlow) on the middle left and the firm information (address, tel, fax, website, email) on right side.  I am open to suggestions if you have better ideas.
Updates

Here are some comments on the initial 8 designs:

a) I am just interested in a font treatment of our firm name, "Harlow & Harlow, P.C."  I do not want any graphics like a gavel or shield. 

b) The full name of the firm must be in the logo.  So I cannot use designs that only have "H & H"

c) EXAMPLES: Here are two websites with examples of law firm logos that just have the firm name.  These are just samples to give you a general idea of what I am looking for.  Check out:  www.qx-legalco.com and www.tarrowmeade-law.com 

In short, I am looking for a simple, clean design that will look modern enough for our website but is also conservative enough to be on letterhead that gets sent to judges and other lawyers.

Also, the sample letterhead is now loaded in the brief so you can see the information I need included in the new letterhead.

Thanks.

Target Market(s)

businesses and corporations.

Industry/Entity Type

Law Firm

Logo Text

Harlow & Harlow, P.C.

Requirements
Must have
• Firm name, "Harlow & Harlow, P.C."

```html
<!DOCTYPE html>
<html lang="en">
<head>
<meta charset="utf-8">
<title>Harlow &amp; Harlow, P.C. — Identity and Stationery</title>
<link rel="stylesheet" href="https://fonts.googleapis.com/css2?family=Oranienbaum&display=swap">
<style>
  :root {
    --crimson: #b00040;
    --sage: #a8a98a;
    --paper: #ffffff;
    --frame: #3a3a3a;
  }
  * { margin: 0; padding: 0; box-sizing: border-box; }
  html, body { width: 848px; height: 1200px; overflow: hidden; background: var(--paper); }
  body { position: relative; font-family: "Oranienbaum", Georgia, serif; color: var(--crimson); }

  .wordmark {
    position: absolute;
    color: var(--crimson);
    font-family: "Oranienbaum", Georgia, serif;
    font-weight: 400;
    white-space: nowrap;
    line-height: 1;
  }
  .wordmark--hero { left: 75px; top: 130px; font-size: 66px; letter-spacing: -1px; }
  .wordmark--letterhead { left: 180px; top: 318px; font-size: 24px; letter-spacing: -0.4px; }
  .wordmark--card { left: 461px; width: 345px; text-align: center; top: 572px; font-size: 26px; letter-spacing: -0.4px; }

  .letterhead {
    position: absolute;
    left: 149px; top: 249px;
    width: 632px; height: 895px;
    border: 1px solid var(--frame);
    background: var(--paper);
  }
  .letterhead__divider {
    position: absolute;
    left: 377px; top: 279px;
    width: 1px; height: 91px;
    background: var(--sage);
  }
  .letterhead__offices {
    position: absolute;
    left: 386px; top: 297px;
    line-height: 1;
  }
  .letterhead__title { font-size: 15px; letter-spacing: 1px; margin-bottom: 1px; }
  .letterhead__line { font-size: 7.4px; line-height: 9.2px; letter-spacing: 0.3px; white-space: nowrap; }

  .letterhead__contact {
    position: absolute;
    left: 172px; top: 1033px;
    font-size: 13px;
    line-height: 15.4px;
    letter-spacing: 0.4px;
    font-style: normal;
  }

  .card {
    position: absolute;
    left: 461px;
    width: 345px; height: 169px;
  }
  .card--front { top: 482px; background: var(--paper); border: 1px solid var(--frame); }
  .card--back { top: 665px; background: var(--crimson); color: var(--paper); }
  .card__name {
    position: absolute;
    left: 22px; top: 44px;
    font-size: 16px;
    letter-spacing: 1px;
  }
  .card__details {
    position: absolute;
    left: 22px; top: 66px;
    font-size: 10.5px;
    line-height: 12.2px;
    letter-spacing: 0.4px;
    font-style: normal;
  }
</style>
</head>
<body>
  <div class="wordmark wordmark--hero">Harlow &amp; Harlow P.C.</div>

  <section class="letterhead" aria-label="Letterhead"></section>
  <div class="wordmark wordmark--letterhead">Harlow &amp; Harlow P.C.</div>
  <div class="letterhead__divider"></div>
  <div class="letterhead__offices">
    <div class="letterhead__title">LAW OFFICES</div>
    <div class="letterhead__line">MARTIN E. HARLOW</div>
    <div class="letterhead__line">COLIN J. HARLOW</div>
    <div class="letterhead__line">WALTER HARLOW (1916-1994)</div>
    <div class="letterhead__line">Admitted to practice District of Columbia . Maryland . New York</div>
  </div>
  <address class="letterhead__contact">
    2710 Larkspur Avenue<br>
    Fairhaven, MD 20999<br>
    T: 301.555.0142<br>
    F: 301.555.0187<br>
    E: martin.harlow@harlowpc-law.com<br>
    www.harlowpc-law.com
  </address>

  <section class="card card--front" aria-label="Business card front"></section>
  <div class="wordmark wordmark--card">Harlow &amp; Harlow P.C.</div>

  <section class="card card--back" aria-label="Business card back">
    <div class="card__name">MARTIN E. HARLOW</div>
    <address class="card__details">
      2710 Larkspur Avenue<br>
      Fairhaven, MD 20999<br>
      T: 301.555.0142<br>
      F: 301.555.0187<br>
      E: martin.harlow@harlowpc-law.com<br>
      www.harlowpc-law.com
    </address>
  </section>
</body>
</html>
```